Quality Improvement Software for healthcare agencies needs a website.

VORTEL218 is a software for hospices and home health agencies to manage their Quality Assurance Performance Improvement programs to remain complaint with the standards set by Sanavox and the Bureau of Clinical Oversight. The web accessible software-as-a-service provides an easy, turn-key way for agencies to organize all the information they need to manage and track.

Coding

Coded - Design and coding required

Number of Pages Required

4 page

```html
<!DOCTYPE html>
<html lang="en">
<head>
<meta charset="utf-8">
<title>VORTEL218 — Quality Improvement for Healthcare Agencies</title>
<link rel="stylesheet" href="https://fonts.googleapis.com/css2?family=Poppins:wght@300;400;500;600;700&display=swap">
<style>
:root{
  --blue:#22b0f5;
  --navy:#1b2a4a;
  --text:#5e6572;
  --muted:#8c93a0;
  --green:#7cc242;
  --orange:#f7931e;
  --yellow:#f5c518;
  --purple:#8b6fe0;
  --card-green:#eef7e6;
  --card-blue:#e6f4fd;
  --card-purple:#efedfb;
  --card-orange:#fdf1e5;
  --card-yellow:#fef8e3;
  --line:#e6e9ef;
  --white:#ffffff;
}
*{box-sizing:border-box;margin:0;padding:0}
html,body{width:1200px;height:3119px;overflow:hidden}
body{position:relative;font-family:'Poppins',sans-serif;color:var(--navy);background:var(--white)}
.abs{position:absolute}
a{color:inherit;text-decoration:none}
.rainbow{height:4px;width:100%;background:linear-gradient(90deg,var(--blue) 0 25%,var(--green) 25% 50%,var(--orange) 50% 75%,var(--yellow) 75% 100%)}
.btn{display:inline-flex;align-items:center;justify-content:center;border-radius:20px;font-size:12px;font-weight:600;background:var(--blue);color:#fff}
.btn-outline{background:transparent;border:1.5px solid var(--navy);color:var(--navy)}

/* hero */
.hero{left:0;top:0;width:1200px;height:529px;background:linear-gradient(120deg,#e4f3fd 0%,#eef8fd 55%,#f1f8ea 100%)}
.brand{display:flex;align-items:center;gap:8px;font-weight:700;font-size:28px;color:var(--navy);letter-spacing:.5px}
.brand-mark{width:22px;height:22px;border-radius:50%;background:var(--blue)}
.nav{display:flex;gap:33px;font-size:12px;color:var(--navy)}
.hero-title{left:111px;top:170px;font-size:53px;line-height:60px;font-weight:300;color:var(--navy)}
.hero-title b{font-weight:700}
.hero-text{left:113px;top:300px;width:410px;font-size:13px;line-height:20px;color:var(--text)}
.hero-photo{left:540px;top:72px;width:560px;height:457px;border-radius:200px 200px 0 0;background:radial-gradient(circle at 55% 40%,#f5d9c4 0%,#c9dcef 45%,#dbeaf5 75%,rgba(234,246,253,0) 100%)}
.mini-card{background:#fff;border-radius:8px;box-shadow:0 6px 18px rgba(27,42,74,.12);font-size:6px;color:var(--navy)}
.icon-bar{left:600px;top:360px;width:172px;height:30px;display:flex;justify-content:space-around;align-items:center;border-radius:15px}
.icon-bar span{width:12px;height:12px;border:1.5px solid #9aa3b3;border-radius:3px}
.icon-bar span:first-child{border-color:var(--blue)}

/* stats */
.stats{left:184px;top:493px;width:831px;height:100px;background:#fff;border-radius:12px;box-shadow:0 10px 30px rgba(27,42,74,.07);display:flex;justify-content:space-around;align-items:center;text-align:center}
.stat-num{font-size:33px;font-weight:700;line-height:38px}
.stat-label{font-size:13px;color:var(--navy)}

/* split sections */
.section-title{font-size:33px;font-weight:700;line-height:38px;color:var(--navy)}
.body-text{font-size:12.5px;line-height:18px;color:var(--text)}
.photo{border-radius:10px}
.glow{border-radius:50%}

/* services */
.services-bg{left:0;top:986px;width:1200px;height:480px;background:linear-gradient(180deg,#fff8f1 0%,#fffdfb 100%)}
.service{width:314px;height:154px;border-radius:8px;padding:22px 20px 0 90px}
.service .ico{position:absolute;left:18px;top:20px;width:56px;height:56px;border-radius:50%;display:flex;align-items:center;justify-content:center}
.service h3{font-size:13.5px;font-weight:600;margin-bottom:8px}
.service p{font-size:10.5px;line-height:16px;color:var(--text);margin-bottom:9px}
.service a{font-size:11.5px;font-weight:600;text-decoration:underline}
.cta{background:var(--blue);color:#fff;text-align:center;padding:20px 30px 0}
.cta h3{font-size:16px;font-weight:600;line-height:19px}
.cta p{font-size:11.5px;margin:14px 0 10px}

/* tasks */
.task{width:150px;height:76px;background:#fff;border-radius:6px;box-shadow:0 4px 16px rgba(27,42,74,.06);display:flex;align-items:center;gap:14px;padding-left:14px;font-size:12px;font-weight:600;line-height:16px}
.task .ico{width:54px;height:54px;flex:none;border-radius:50%;background:#e3f3fd;display:flex;align-items:center;justify-content:center}

/* blog */
.post{width:314px;height:342px;background:#fff;border-radius:8px;box-shadow:0 6px 22px rgba(27,42,74,.06);overflow:hidden}
.post-img{height:164px}
.post-date{position:absolute;left:20px;top:126px;width:150px;height:38px;background:var(--blue);border-radius:12px 12px 0 0;color:#fff;font-size:12.5px;font-weight:600;display:flex;align-items:center;justify-content:center}
.post-body{padding:20px 20px 0}
.post-body h3{font-size:14px;font-weight:600;line-height:16px;margin-bottom:20px;width:230px;height:32px}
.post-body p{font-size:11.5px;line-height:17.5px;color:var(--text);margin-bottom:16px;width:260px}
.post-body a{font-size:11.5px;font-weight:600;color:var(--blue);text-decoration:underline}

/* signup */
.signup{left:0;top:2635px;width:1200px;height:245px;background:#eaf6fd}
.field{height:43px;border-radius:22px;background:#fff;font-size:12px;color:var(--muted);display:flex;align-items:center;padding-left:24px}

/* footer */
.footer-nav{display:flex;gap:32px;font-size:12px;color:var(--navy)}
.social{display:flex;gap:8px}
.social span{width:19px;height:19px;border-radius:50%;background:var(--blue)}
</style>
</head>
<body>

<div class="abs rainbow" style="top:0;left:0;z-index:3"></div>

<!-- Hero -->
<section class="abs hero">
  <div class="abs hero-photo" role="img" aria-label="Smiling family of three: mother, father and toddler"></div>

  <div class="abs mini-card" style="left:1008px;top:137px;width:83px;height:96px;padding:8px">
    <div style="color:var(--blue);font-weight:600;line-height:8px">Hi,<br>Welcome back.</div>
    <div style="margin-top:10px;height:6px;border-radius:3px;background:#eef1f5"></div>
    <div style="margin-top:8px;height:6px;border-radius:3px;background:#eef1f5"></div>
    <div style="margin-top:14px;height:7px;border-radius:3px;background:var(--blue);color:#fff;text-align:center;font-size:5px;line-height:7px">Login</div>
  </div>
  <div class="abs mini-card" style="left:947px;top:388px;width:118px;height:50px;padding:5px 6px">
    <div style="font-weight:600">Calendar</div>
    <div style="text-align:center;margin-top:2px">July 2021</div>
    <div style="display:flex;justify-content:space-between;margin-top:5px;font-size:5px;color:var(--muted)">
      <span>‹</span><span>5</span><span>6</span><span style="background:var(--purple);color:#fff;border-radius:3px;padding:0 2px">7</span><span>8</span><span>9</span><span>10</span><span>11</span><span>›</span>
    </div>
  </div>
  <div class="abs mini-card icon-bar"><span></span><span></span><span></span><span></span><span></span></div>

  <div class="abs brand" style="left:111px;top:36px"><span class="brand-mark"></span>VORTEL218</div>
  <nav class="abs nav" style="left:460px;top:41px">
    <a>How We Help</a><a>Who We Are</a><a>Platform</a><a>Resources</a><a>Blog</a>
  </nav>
  <svg class="abs" style="left:917px;top:40px" width="18" height="18" viewBox="0 0 18 18" fill="none" stroke="#1b2a4a" stroke-width="1.6"><circle cx="7.5" cy="7.5" r="6"/><path d="M12 12l5 5"/></svg>
  <a class="abs btn" style="left:973px;top:31px;width:113px;height:36px">Get In Touch</a>

  <h1 class="abs hero-title"><b>Healthcare</b> for<br>Family's Health</h1>
  <p class="abs hero-text">Let's check how your dental health is our professionals with complete and modern facilities.</p>
  <a class="abs btn" style="left:113px;top:360px;width:113px;height:34px">Get Started</a>
  <a class="abs btn btn-outline" style="left:240px;top:360px;width:112px;height:34px">Learn More</a>
</section>

<!-- Stats -->
<div class="abs stats">
  <div><div class="stat-num" style="color:var(--blue)">400+</div><div class="stat-label">Patients Daily</div></div>
  <div><div class="stat-num" style="color:var(--green)">10+</div><div class="stat-label">Years on the Market</div></div>
  <div><div class="stat-num" style="color:var(--orange)">300</div><div class="stat-label">Qualified Doctors</div></div>
  <div><div class="stat-num" style="color:var(--yellow)">30</div><div class="stat-label">Clinic Locations</div></div>
</div>

<!-- Track health -->
<section>
  <div class="abs glow" style="left:85px;top:630px;width:260px;height:260px;background:radial-gradient(circle,rgba(247,147,30,.07) 0%,rgba(247,147,30,0) 70%)"></div>
  <div class="abs photo" style="left:160px;top:684px;width:357px;height:239px;background:linear-gradient(180deg,#cfdbe6 0%,#e8d9cc 60%,#b9a999 100%)" role="img" aria-label="Woman meditating on a beach at sunset"></div>
  <div class="abs" style="left:298px;top:755px;width:100px;height:100px;border-radius:50%;background:rgba(34,176,245,.25);display:flex;align-items:center;justify-content:center">
    <div style="width:64px;height:64px;border-radius:50%;background:var(--blue);display:flex;align-items:center;justify-content:center">
      <svg width="22" height="24" viewBox="0 0 22 24"><path d="M3 2l17 10L3 22z" fill="#fff"/></svg>
    </div>
  </div>
  <div class="abs mini-card" style="left:444px;top:658px;width:101px;height:153px;padding:6px">
    <div style="display:flex;gap:4px;align-items:center"><span style="width:12px;height:12px;border-radius:50%;background:var(--blue)"></span><span style="line-height:7px"><b>Lena Hart</b><br>Online</span></div>
    <div style="margin-top:16px;width:68px;height:18px;border-radius:5px;background:#eef1f5"></div>
    <div style="margin-top:6px;width:74px;height:14px;border-radius:5px;background:#eef1f5"></div>
    <div style="margin:8px 0 0 36px;width:56px;height:14px;border-radius:5px;background:var(--blue)"></div>
    <div style="margin-top:30px;height:9px;border-radius:5px;background:#eef1f5"></div>
  </div>
  <div class="abs mini-card" style="left:111px;top:845px;width:149px;height:45px;padding:5px 7px">
    <div style="font-weight:600">Highlight update</div>
    <div style="display:flex;gap:9px;margin-top:6px"><span style="width:14px;height:14px;border-radius:50%;background:#f6d3c4"></span><span style="width:14px;height:14px;border-radius:50%;border:1.5px solid var(--purple)"></span><span style="width:14px;height:14px;border-radius:50%;border:1.5px solid var(--purple)"></span><span style="width:14px;height:14px;border-radius:50%;border:1.5px solid var(--purple)"></span><span style="width:14px;height:14px;border-radius:50%;border:1.5px solid var(--purple)"></span></div>
  </div>

  <h2 class="abs section-title" style="left:656px;top:710px;width:420px">Track the state of your health daily</h2>
  <p class="abs body-text" style="left:657px;top:808px;width:445px;font-size:12px">The program allows you not only to record your emotions, develop your emotional vocabulary, but also to keep a thoughts and actions journal for further analysis and reflection. This section will be especially useful if you are not yet able to receive psychological help.</p>
</section>

<!-- Services -->
<div class="abs services-bg"></div>
<section>
  <h2 class="abs section-title" style="left:0;width:1200px;top:1018px;text-align:center">Our Medical Services</h2>
  <p class="abs body-text" style="left:0;width:1200px;top:1069px;text-align:center">Molestiae non recusandae earum rerum hic tenetur asa piente delectus.</p>

  <article class="abs service" style="left:113px;top:1120px;background:var(--card-green)">
    <div class="ico" style="background:#d8eec6"><svg width="28" height="26" viewBox="0 0 28 26" fill="none" stroke="#6bb03a" stroke-width="1.6"><path d="M14 24S2 16 2 8a6 6 0 0 1 12-1 6 6 0 0 1 12 1c0 8-12 16-12 16z"/><path d="M5 13h6l2-4 3 7 2-3h5"/></svg></div>
    <h3>Cardiologist</h3><p>In sit amet ex vel metus facilisis venenatis. Suspendisse blandit dictum sollicitudin.</p><a style="color:var(--green)">Read More</a>
  </article>
  <article class="abs service" style="left:443px;top:1120px;background:var(--card-blue)">
    <div class="ico" style="background:#cfeafb"><svg width="28" height="26" viewBox="0 0 28 26" fill="none" stroke="#39a9e6" stroke-width="1.6"><path d="M14 2v10M14 10l-4 3M14 10l4 3"/><path d="M10 8C5 8 3 18 3 22c0 2 5 1 7-1V8zM18 8c5 0 7 10 7 14 0 2-5 1-7-1V8z"/></svg></div>
    <h3>Pulmonary</h3><p>In sit amet ex vel metus facilisis venenatis. Suspendisse blandit dictum sollicitudin.</p><a style="color:var(--blue)">Read More</a>
  </article>
  <article class="abs service" style="left:773px;top:1120px;background:var(--card-purple)">
    <div class="ico" style="background:#ddd6f8"><svg width="30" height="26" viewBox="0 0 30 26" fill="none" stroke="#8b6fe0" stroke-width="1.6"><path d="M9 8c0-3 12-3 12 0v6c0 3-3 4-3 7v3h-6v-3c0-3-3-4-3-7z"/><path d="M9 10C6 6 3 7 3 10s3 3 4 2M21 10c3-4 6-3 6 0s-3 3-4 2"/></svg></div>
    <h3>Gynecology</h3><p>In sit amet ex vel metus facilisis venenatis. Suspendisse blandit dictum sollicitudin.</p><a style="color:var(--purple)">Read More</a>
  </article>
  <article class="abs service" style="left:113px;top:1288px;background:var(--card-orange)">
    <div class="ico" style="background:#fcdcbc"><svg width="30" height="20" viewBox="0 0 30 20" fill="none" stroke="#f08a24" stroke-width="1.6"><path d="M2 10s5-8 13-8 13 8 13 8-5 8-13 8S2 10 2 10z"/><circle cx="15" cy="10" r="4"/></svg></div>
    <h3>Ophthalmology</h3><p>In sit amet ex vel metus facilisis venenatis. Suspendisse blandit dictum sollicitudin.</p><a style="color:var(--orange)">Read More</a>
  </article>
  <article class="abs service" style="left:443px;top:1288px;background:var(--card-yellow)">
    <div class="ico" style="background:#fcebb0"><svg width="28" height="24" viewBox="0 0 28 24" fill="none" stroke="#e9b10f" stroke-width="1.6"><path d="M6 18c-4 0-5-5-2-7-1-4 3-7 6-5 2-3 7-3 9 0 4-1 7 3 5 6 2 3 0 6-3 6h-5v4h-4v-4z"/></svg></div>
    <h3>Psychiatry</h3><p>In sit amet ex vel metus facilisis venenatis. Suspendisse blandit dictum sollicitudin.</p><a style="color:var(--yellow)">Read More</a>
  </article>
  <article class="abs service cta" style="left:773px;top:1288px">
    <h3>We Provide Best Medical Treatment.</h3>
    <p>Reprehenderit in voluta zesse.</p>
    <a class="btn" style="background:#fff;color:var(--blue);width:136px;height:32px;font-weight:500">Book Appointment</a>
  </article>
</section>

<!-- Tasks -->
<section>
  <h2 class="abs section-title" style="left:111px;top:1498px;width:300px;line-height:44px">Easy tasks to improve your overall health</h2>
  <p class="abs body-text" style="left:111px;top:1646px;width:270px;font-size:12px">This is a unique program that will help you track, maintain and improve your health by performing simple and accessible tasks.</p>

  <div class="abs task" style="left:429px;top:1508px"><span class="ico" style="color:var(--blue);font-size:15px;font-weight:500">Z<sub style="font-size:11px">z</sub></span>Sleep</div>
  <div class="abs task" style="left:598px;top:1508px"><span class="ico"><svg width="28" height="16" viewBox="0 0 28 16" fill="none" stroke="#39a9e6" stroke-width="1.6"><rect x="4" y="2" width="4" height="12" rx="1"/><rect x="20" y="2" width="4" height="12" rx="1"/><path d="M1 8h3M8 8h12M24 8h3"/></svg></span>Exercise</div>
  <div class="abs task" style="left:768px;top:1508px"><span class="ico"><svg width="20" height="26" viewBox="0 0 20 26" fill="none" stroke="#39a9e6" stroke-width="1.6"><circle cx="11" cy="3" r="2"/><path d="M10 7l-3 8 5 3 1 7M9 11l-5 3M10 8l5 5 3-1M7 15l-3 9"/></svg></span>Take a<br>walk</div>
  <div class="abs task" style="left:937px;top:1508px"><span class="ico"><svg width="26" height="24" viewBox="0 0 26 24" fill="none" stroke="#39a9e6" stroke-width="1.6"><rect x="2" y="2" width="14" height="12" rx="1"/><rect x="10" y="10" width="14" height="12" rx="1"/></svg></span>Hobby</div>
  <div class="abs task" style="left:429px;top:1605px"><span class="ico"><svg width="22" height="22" viewBox="0 0 22 22" fill="none" stroke="#39a9e6" stroke-width="1.6"><path d="M5 2l15 9L5 20z"/></svg></span>Listen to<br>Music</div>
  <div class="abs task" style="left:598px;top:1605px"><span class="ico"><svg width="24" height="26" viewBox="0 0 24 26" fill="none" stroke="#39a9e6" stroke-width="1.6"><circle cx="12" cy="10" r="8"/><circle cx="12" cy="10" r="4"/><path d="M7 17l-2 8 7-3 7 3-2-8"/></svg></span>Reward</div>
  <div class="abs task" style="left:768px;top:1605px"><span class="ico"><svg width="24" height="24" viewBox="0 0 24 24" fill="none" stroke="#39a9e6" stroke-width="1.6"><path d="M9 2S3 11 3 15a6 6 0 0 0 12 0C15 11 9 2 9 2z"/><path d="M17 8s-3 5-3 7"/></svg></span>Water</div>
  <div class="abs task" style="left:937px;top:1605px"><span class="ico"><svg width="28" height="22" viewBox="0 0 28 22" fill="none" stroke="#39a9e6" stroke-width="1.6"><path d="M14 2c4 4 4 11 0 17-4-6-4-13 0-17z"/><path d="M14 19C9 18 5 13 5 7c4 1 7 4 9 8M14 19c5-1 9-6 9-12-4 1-7 4-9 8"/><path d="M2 13c3 4 7 6 12 6s9-2 12-6"/></svg></span>Meditate</div>
</section>

<!-- Statistics -->
<section>
  <div class="abs photo" style="left:144px;top:1766px;width:314px;height:238px;background:linear-gradient(135deg,#5aa9d6 0%,#a8cfe4 50%,#e8eef2 100%)" role="img" aria-label="Doctor high-fiving a young patient with his father in a clinic"></div>
  <div class="abs mini-card" style="left:436px;top:1775px;width:82px;height:150px;padding:6px">
    <div style="font-weight:600">User review</div>
    <div style="display:flex;gap:3px;align-items:center;margin-top:6px"><span style="width:12px;height:12px;border-radius:50%;background:var(--purple)"></span>Lena Hart</div>
    <div style="color:var(--purple);margin-top:4px;letter-spacing:1px">★★★★★</div>
    <div style="margin-top:6px;font-weight:600">Satisfied</div>
    <div style="margin-top:4px;height:3px;background:#eef1f5"></div>
    <div style="margin-top:3px;height:3px;background:#eef1f5"></div>
    <div style="margin-top:3px;height:3px;background:#eef1f5"></div>
    <div style="margin-top:3px;height:3px;width:60%;background:#eef1f5"></div>
    <div style="margin-top:14px;height:7px;border-radius:4px;background:var(--purple)"></div>
    <div style="margin-top:4px;height:7px;border-radius:4px;border:1px solid #dcdff0"></div>
  </div>
  <div class="abs mini-card" style="left:111px;top:1901px;width:101px;height:85px;padding:5px">
    <div style="font-weight:600">Patient visits</div>
    <svg width="90" height="62" viewBox="0 0 90 62" fill="none">
      <path d="M2 48h86M2 36h86M2 24h86" stroke="#eef1f5" stroke-width="1"/>
      <path d="M4 44l10-4 8 6 10-12 10 6 12-16 10 10 10-4 12 8" stroke="#22b0f5" stroke-width="1.5"/>
      <rect x="50" y="8" width="18" height="8" rx="2" fill="#22b0f5"/>
    </svg>
  </div>

  <h2 class="abs section-title" style="left:654px;top:1812px">Useful statistics</h2>
  <p class="abs body-text" style="left:656px;top:1866px;width:445px;font-size:12px">If you are already seeing a psychologist or a mental health professional, you can use the acquired knowledge while attending the sessions!</p>
  <a class="abs btn" style="left:655px;top:1923px;width:123px;height:33px">Start Now</a>
</section>

<!-- Blog -->
<section>
  <h2 class="abs section-title" style="left:0;width:1200px;top:2100px;text-align:center">Learn new with us</h2>

  <article class="abs post" style="left:113px;top:2165px">
    <div class="post-img" style="background:linear-gradient(135deg,#dfe7ec 0%,#b9ccd8 60%,#8fa9bb 100%)" role="img" aria-label="Masked doctor consulting with a patient"></div>
    <div class="post-date">DECEMBER 17, 2021</div>
    <div class="post-body"><h3>Get The Exercise Limited Mobility</h3><p>It is a long established fact that a reader will be distracted by the readable content of a page when looking at its layout.</p><a>Read More</a></div>
  </article>
  <article class="abs post" style="left:443px;top:2165px">
    <div class="post-img" style="background:linear-gradient(135deg,#e8d8cc 0%,#d9b9a1 55%,#bfa08a 100%)" role="img" aria-label="Doctor high-fiving a smiling girl and her mother"></div>
    <div class="post-date">DECEMBER 05, 2021</div>
    <div class="post-body"><h3>Transfusion Strategy And Heart Surgery</h3><p>It is a long established fact that a reader will be distracted by the readable content of a page when looking at its layout.</p><a>Read More</a></div>
  </article>
  <article class="abs post" style="left:773px;top:2165px">
    <div class="post-img" style="background:linear-gradient(135deg,#eef0f2 0%,#b8cfe0 55%,#6e9ec4 100%)" role="img" aria-label="Nurses caring for an elderly patient in a hospital bed"></div>
    <div class="post-date">DECEMBER 05, 2021</div>
    <div class="post-body"><h3>Latest Equipment For The Heart Treatment</h3><p>It is a long established fact that a reader will be distracted by the readable content of a page when looking at its layout.</p><a>Read More</a></div>
  </article>

  <a class="abs btn" style="left:533px;top:2539px;width:135px;height:33px">Discover All Blogs</a>
</section>

<!-- Signup -->
<section class="abs signup">
  <h2 class="abs section-title" style="left:0;width:1200px;top:38px;text-align:center">Start a stress-free life</h2>
  <p class="abs body-text" style="left:0;width:1200px;top:94px;text-align:center">Complete a simple registration and start changing your life today!</p>
  <div class="abs field" style="left:113px;top:138px;width:314px">Name</div>
  <div class="abs field" style="left:443px;top:138px;width:390px">Email</div>
  <a class="abs btn" style="left:846px;top:138px;width:240px;height:43px;border-radius:22px;font-size:12.5px">Registration</a>
</section>

<!-- Footer -->
<footer>
  <div class="abs brand" style="left:0;width:1200px;justify-content:center;top:2922px"><span class="brand-mark"></span>VORTEL218</div>
  <nav class="abs footer-nav" style="left:0;width:1200px;justify-content:center;top:2983px">
    <a>How We Help</a><a>Who We Are</a><a>Platform</a><a>Resources</a><a>Blog</a>
  </nav>
  <div class="abs" style="left:0;top:3034px;width:530px;height:1px;background:var(--line)"></div>
  <div class="abs" style="left:662px;top:3034px;width:538px;height:1px;background:var(--line)"></div>
  <div class="abs social" style="left:550px;top:3025px"><span></span><span></span><span></span><span></span></div>
  <p class="abs" style="left:0;width:1200px;top:3069px;text-align:center;font-size:10.5px;color:var(--navy)">Copyright © 2023. All rights reserved.</p>
  <div class="abs rainbow" style="left:0;top:3115px"></div>
</footer>

</body>
</html>
```